Payroll Brochure

Create a brochure with the copy i have provided . A simple easy tp read brochure that shows wat we do we handle payroll taxes insurance 401k etc

```html
<!DOCTYPE html>
<html lang="en">
<head>
<meta charset="utf-8">
<title>Corvane Payroll Services Brochure</title>
<link href="https://fonts.googleapis.com/css2?family=Open+Sans:wght@400;600;700&display=swap" rel="stylesheet">
<style>
  :root {
    --cream: #f3ede2;
    --red: #d32a3a;
    --maroon: #9c2430;
    --white: #ffffff;
  }
  * { margin: 0; padding: 0; box-sizing: border-box; }
  html, body { width: 849px; height: 1200px; overflow: hidden; }
  body { font-family: "Open Sans", Arial, sans-serif; background: var(--cream); }

  .brochure { position: relative; width: 849px; height: 1200px; background: var(--cream); }

  .brand {
    position: absolute; left: 133px; top: 30px;
    display: flex; align-items: center; gap: 8px;
    font-size: 22px; font-weight: 700; color: var(--maroon);
  }
  .brand-dot { width: 18px; height: 18px; border-radius: 50%; background: var(--maroon); }

  .content-panel {
    position: absolute; left: 283px; top: 0; width: 566px; height: 1200px;
    background: var(--red);
  }

  .service-visual { position: absolute; left: 113px; width: 170px; }
  .service-title {
    position: absolute; left: 118px; width: 165px;
    font-size: 24px; font-weight: 600; line-height: 1.15; color: var(--maroon);
  }

  .feature-group { position: absolute; left: 310px; width: 505px; color: var(--white); }
  .feature { margin-bottom: 14px; }
  .feature-title {
    font-size: 12px; font-weight: 700; text-transform: uppercase; letter-spacing: 0.3px;
    margin-bottom: 3px;
  }
  .feature-text { font-size: 12.5px; line-height: 1.4; }
</style>
</head>
<body>
<main class="brochure">
  <div class="brand"><span class="brand-dot"></span>Corvane</div>

  <section class="content-panel"></section>

  <!-- Payroll -->
  <div class="service-visual" style="top:160px;height:200px;background:linear-gradient(135deg,#c9c4bb,#8d8a86);" role="img" aria-label="Photo of a payroll worksheet with a pen"></div>
  <h2 class="service-title" style="top:385px;">Payroll</h2>
  <div class="feature-group" style="top:172px;">
    <div class="feature">
      <p class="feature-title">Flexible</p>
      <p class="feature-text">Corvane's flexible and powerful payroll module allows you the ability to grow you're your business by meeting your unique needs. Supporting payrolls for very large to very small companies.</p>
    </div>
    <div class="feature">
      <p class="feature-title">Efficient</p>
      <p class="feature-text">Get payroll done efficiently and accurately by relying on our flexible design to handle even the most complex payroll needs.</p>
    </div>
    <div class="feature">
      <p class="feature-title">Grow without growing pains</p>
      <p class="feature-text">Corvane's technology and design is able to allow you to scale your business without adding all the incremental costs typically required.</p>
    </div>
  </div>

  <!-- Tax Reporting -->
  <div class="service-visual" style="top:428px;height:90px;background:linear-gradient(135deg,#d8d6d2,#6f7377);" role="img" aria-label="Photo of a tax form with a calculator and glasses"></div>
  <h2 class="service-title" style="top:532px;">Tax Reporting &amp; Payments</h2>
  <div class="feature-group" style="top:440px;">
    <div class="feature">
      <p class="feature-title">Accurate</p>
      <p class="feature-text">all payroll taxes (federal, state, local) are calculated accurately. Additionally, we determine proper local tax jurisdictions based on the employee home and work addresses.</p>
    </div>
    <div class="feature">
      <p class="feature-title">Complete</p>
      <p class="feature-text">Federal, State, and Local withholding taxes as well as State and Federal Unemployment taxes are provided. Tax payments are integrated into the Accounts Payable and General Ledger modules.</p>
    </div>
  </div>

  <!-- Human Resources -->
  <div class="service-visual" style="top:625px;height:125px;background:linear-gradient(135deg,#5d6f86,#2f3a48);" role="img" aria-label="Photo of a hand touching a human resources network graphic"></div>
  <h2 class="service-title" style="top:765px;">Human Resources</h2>
  <div class="feature-group" style="top:655px;">
    <div class="feature">
      <p class="feature-text">With our online HR tools, you can empower yourself to take control of your human resource needs or let us do it.</p>
    </div>
    <div class="feature">
      <p class="feature-title">Get big company services</p>
      <p class="feature-text">by using our online tools in conjunction with your service team, you will have access to HR services only afforded by some of the largest companies.</p>
    </div>
    <div class="feature">
      <p class="feature-title">Library</p>
      <p class="feature-text">our online document library lets you and employees create your own library of information accessible at any time. Employees can upload documents and forms that can be kept in history as long as needed.</p>
    </div>
  </div>

  <!-- Benefit Enrolment -->
  <div class="service-visual" style="top:875px;height:130px;background:linear-gradient(135deg,#e6e2dc,#a7a39c);" role="img" aria-label="Photo of a piggy bank on a table"></div>
  <h2 class="service-title" style="top:1085px;">Benefit Enrolment</h2>
  <div class="feature-group" style="top:918px;">
    <div class="feature">
      <p class="feature-title">Easy and quick enrollment</p>
      <p class="feature-text">Our intuitive user experience quickly walks employees through their benefit enrollment process and allows them to compare different plans and select those that best meet their life needs.</p>
    </div>
    <div class="feature">
      <p class="feature-title">Flexible benefit plans and easy setup options</p>
      <p class="feature-text">Offer your clients top-tier benefit plans or administer their plans in an easy to use, yet flexible benefit administration module.</p>
    </div>
    <div class="feature">
      <p class="feature-title">You pick</p>
      <p class="feature-text">with our flexible contribution setup features, you can contribute in any manner to your employees' benefits while the system automatically processes them through payroll</p>
    </div>
  </div>
</main>
</body>
</html>
```